Mezzanine Floor Manufacturer looking for a new business card design

We manufacture mezzanine floors and are providers of racking systems. We provide a range of items/services - simple rack repairs , full warehouse fit outs , manufacturer and install mezzanine floors , partitioning and large turnkey projects. Recently had a new website - www.corrowden-racking.co.uk and would like our business cards updating aswell . Our current card is single sided in the old logo colours (pdf attached) and needs updating.

Target Market(s)

We deal with large projects/ multi national companies and also smaller projects and companies throughout the UK ranging from a single warehouse to a large multi site company.

Industry/Entity Type

Business

Contact Information for Business Card

Will have job title,tel no's, email ,website address etc like example pdf

Requirements
Must have
• Hi - needs to use the colours of the logo & new website. Card needs to be professional

```html
<!DOCTYPE html>
<html lang="en">
<head>
<meta charset="utf-8">
<title>Corrowden business card</title>
<link href="https://fonts.googleapis.com/css2?family=Open+Sans:wght@400;600;700;800&display=swap" rel="stylesheet">
<style>
:root{
  --red:#d2382a;
  --logo-red:#c8202a;
  --black:#000;
  --white:#fff;
  --ink:#1a1a1a;
  --page:#e9e9e9;
}
*{box-sizing:border-box;margin:0;padding:0}
html,body{width:1200px;height:900px;overflow:hidden}
body{background:var(--page);font-family:"Open Sans",Arial,sans-serif;position:relative}
.card{position:absolute;width:560px;height:320px;border-radius:22px;overflow:hidden;box-shadow:0 6px 18px rgba(0,0,0,.18)}
.card-front{left:320px;top:100px;background:var(--white)}
.card-back{left:320px;top:480px;background:var(--red)}

.brand-mark{position:absolute;left:0;right:0;top:52px;display:flex;justify-content:center;align-items:center;gap:14px}
.brand-dot{width:26px;height:26px;border-radius:50%;background:var(--logo-red)}
.brand-name{font-weight:800;font-size:64px;color:var(--logo-red);letter-spacing:2px;line-height:1}

.services{position:absolute;left:0;right:0;top:150px;text-align:center;color:var(--ink);font-weight:600;font-size:13px;line-height:17px;letter-spacing:.4px;text-transform:uppercase}
.services-title{color:var(--red);font-weight:700;font-size:15px}
.web-rule{position:absolute;left:26px;right:26px;top:262px;display:flex;align-items:center;gap:10px;font-size:14px;font-weight:600;color:var(--ink);letter-spacing:.5px}
.web-rule::before,.web-rule::after{content:"";flex:1;height:1px;background:var(--red)}
.web-rule .accent{color:var(--red)}

.back-shape{position:absolute;inset:0}
.back-mark{position:absolute;left:160px;top:80px;display:flex;align-items:center;gap:10px}
.back-mark .brand-dot{width:18px;height:18px;background:var(--red)}
.back-mark .brand-name{font-size:44px;color:var(--white)}
.contact{position:absolute;right:30px;top:26px;text-align:right;color:var(--white);font-size:13px;line-height:17px;font-weight:600}
.company{font-size:24px;font-weight:800;letter-spacing:2px;margin-bottom:12px}
.person{color:var(--red);font-size:20px;font-weight:800;letter-spacing:1px;line-height:22px}
.role{font-size:12px;letter-spacing:1px;margin-bottom:6px}
.address{margin-bottom:4px}
.line{display:flex;justify-content:flex-end;align-items:center;gap:8px}
.line svg{width:11px;height:11px;fill:var(--red)}
.online{position:absolute;right:30px;top:256px;text-align:right;color:var(--white);font-size:13px;line-height:17px;font-weight:600}
</style>
</head>
<body>

<section class="card card-front">
  <div class="brand-mark">
    <span class="brand-dot"></span>
    <span class="brand-name">CRH</span>
  </div>
  <div class="services">
    <div class="services-title">Services</div>
    <div>Rack repairs</div>
    <div>Full warehouse fit outs</div>
    <div>Manufacturer and install mezzanine floors</div>
    <div>Partitioning and large turnkey projects.</div>
  </div>
  <div class="web-rule"><span>www.<span class="accent">corrowden-racking</span>.co.uk</span></div>
</section>

<section class="card card-back">
  <svg class="back-shape" viewBox="0 0 560 320" preserveAspectRatio="none" aria-hidden="true">
    <path d="M158,0 C40,120 120,310 440,320 H560 V0 Z" fill="var(--white)"/>
    <path d="M172,0 C60,120 140,300 452,320 H560 V0 Z" fill="var(--black)"/>
  </svg>
  <div class="back-mark">
    <span class="brand-dot"></span>
    <span class="brand-name">CRH</span>
  </div>
  <div class="contact">
    <div class="company">CORROWDEN</div>
    <div class="person">DANIEL HARTLEY</div>
    <div class="role">TECHNICAL SALES</div>
    <div class="address">Elmbrook close<br>Fenwick vale business Park<br>Ashby, Westshire AB1 2CD</div>
    <div class="line">01632 960481 <svg viewBox="0 0 10 10"><path d="M2 0h2l1 3-1.5 1a6 6 0 0 0 2.5 2.5L7 5l3 1v2c0 1-1 2-2 2A8 8 0 0 1 0 2c0-1 1-2 2-2z"/></svg></div>
    <div class="line">07700 900312 <svg viewBox="0 0 10 10"><rect x="2.5" y="0" width="5" height="10" rx="1"/></svg></div>
    <div class="line">01632 960795 <svg viewBox="0 0 10 10"><rect x="0" y="3" width="10" height="5" rx="1"/><rect x="2" y="0" width="6" height="3"/></svg></div>
  </div>
  <div class="online">
    <div class="line">daniel@corrowden-racking.co.uk <svg viewBox="0 0 10 10"><path d="M0 2h10v6H0z M0 2l5 4 5-4" fill="none" stroke="var(--red)" stroke-width="1.2"/></svg></div>
    <div class="line">www.corrowden-racking.co.uk <svg viewBox="0 0 10 10"><circle cx="5" cy="5" r="4.4" fill="none" stroke="var(--red)" stroke-width="1.2"/><path d="M1 5h8M5 1v8" stroke="var(--red)" stroke-width="1"/></svg></div>
  </div>
</section>

</body>
</html>
```